Book cover design for modern bagpipe music book

This music book will be A4 in size and requires a design for the front and back cover. The focus is on creating a modern and eye catching design, breaking away from the stereotypes of what people think of when they think of bagpipes. Think the OPPOSITE of a bagpiper in a full kilt standing on top of a mountain playing Lanterns on the Moor!

Book title: Wake Stroll Hum Again

Other front cover text : Music for the bagpipes by Dara Colby

Front cover file ideas uploaded

2 pictures of bagpipes attached.

- The real set of bagpipes give an idea of the correct finer details

- The toy bagpipes perhaps have a better shape with the left 'stick' down

Back cover - No real brief. Keen for it not to be a full block single colour though.

Design requires 3mm bleed for print

Open to ideas and suggestions! Thank you!

```html
<!DOCTYPE html>
<html lang="en">
<head>
<meta charset="utf-8">
<title>Wake Stroll Hum Again – Music for the Bagpipes</title>
<link rel="stylesheet" href="https://fonts.googleapis.com/css2?family=Bebas+Neue&family=Oswald:wght@500;600&display=swap">
<style>
  :root {
    --cover-red: #d21f2e;
    --tartan-red: #d7232f;
    --ink: #111111;
    --paper: #ffffff;
    --ghost-grey: #d9d9d9;
  }
  * { margin: 0; padding: 0; box-sizing: border-box; }
  html, body { width: 927px; height: 1200px; overflow: hidden; background: var(--paper); }
  .cover {
    position: relative;
    width: 927px;
    height: 1200px;
    background: var(--paper);
    overflow: hidden;
    font-family: "Bebas Neue", "Oswald", sans-serif;
  }
  .icon-band {
    position: absolute;
    left: 0; top: 0;
    width: 326px;
    height: 1097px;
    background: var(--cover-red);
  }
  .icon-tile {
    position: absolute;
    left: 38px;
    width: 236px;
    height: 236px;
  }
  .icon-tile svg { display: block; width: 100%; height: 100%; }
  .icon-eat { top: 50px; }
  .icon-sleep { top: 315px; }
  .icon-pipe { top: 580px; }
  .icon-repeat { top: 845px; }
  .pipe-art {
    position: absolute;
    left: 58px; top: 50px;
    width: 120px; height: 136px;
    border-radius: 40% 40% 50% 50%;
    background: linear-gradient(160deg, #ffffff, #e6e6e6);
  }
  .author-tab {
    position: absolute;
    right: 0; top: 0;
    width: 352px;
    height: 92px;
    background: var(--cover-red);
    border-bottom-left-radius: 22px;
    color: var(--paper);
    font-family: "Oswald", sans-serif;
    font-weight: 600;
    font-size: 50px;
    line-height: 92px;
    text-align: center;
    letter-spacing: 0.5px;
  }
  .bagpipe-ghost {
    position: absolute;
    left: 715px; top: 110px;
    width: 212px; height: 800px;
    background: linear-gradient(180deg, rgba(217,217,217,0.25) 0%, var(--ghost-grey) 45%, rgba(217,217,217,0.6) 100%);
    border-radius: 90px 0 0 60px;
  }
  .title {
    position: absolute;
    left: 338px; top: 0;
  }
  .title-word {
    position: absolute;
    left: 0;
    font-size: 236px;
    line-height: 1;
    color: var(--tartan-red);
    letter-spacing: 2px;
    white-space: nowrap;
  }
  .word-1 { top: 80px; }
  .word-2 { top: 342px; }
  .word-3 { top: 592px; }
  .word-4 { top: 846px; }
  .subtitle-bar {
    position: absolute;
    left: 0; bottom: 0;
    width: 927px;
    height: 103px;
    background: var(--ink);
    color: var(--paper);
    font-size: 92px;
    line-height: 108px;
    text-align: center;
    letter-spacing: 1px;
  }
</style>
</head>
<body>
<main class="cover">
  <aside class="icon-band">
    <div class="icon-tile icon-eat">
      <svg viewBox="0 0 236 236" aria-hidden="true">
        <rect x="3" y="3" width="230" height="230" rx="24" fill="#111" stroke="#fff" stroke-width="4"/>
        <g fill="#fff">
          <rect x="30" y="60" width="5" height="45"/>
          <rect x="40" y="60" width="5" height="45"/>
          <rect x="50" y="60" width="5" height="45"/>
          <rect x="30" y="100" width="25" height="12" rx="4"/>
          <rect x="37" y="108" width="11" height="75" rx="5"/>
          <circle cx="118" cy="120" r="62"/>
          <path d="M186 60 C204 70 206 110 200 128 L196 128 L196 183 Q190 190 184 183 Z"/>
        </g>
        <circle cx="118" cy="120" r="48" fill="none" stroke="#111" stroke-width="5"/>
      </svg>
    </div>
    <div class="icon-tile icon-sleep">
      <svg viewBox="0 0 236 236" aria-hidden="true">
        <rect x="3" y="3" width="230" height="230" rx="24" fill="#111" stroke="#fff" stroke-width="4"/>
        <g fill="#fff">
          <rect x="28" y="70" width="14" height="110" rx="3"/>
          <rect x="194" y="112" width="14" height="68" rx="3"/>
          <rect x="28" y="138" width="180" height="16" rx="3"/>
          <circle cx="68" cy="104" r="17"/>
          <path d="M92 92 H176 Q192 92 192 108 V132 H92 Z"/>
          <rect x="48" y="124" width="44" height="8" rx="3"/>
        </g>
      </svg>
    </div>
    <div class="icon-tile icon-pipe">
      <svg viewBox="0 0 236 236" aria-hidden="true">
        <rect x="3" y="3" width="230" height="230" rx="24" fill="#111" stroke="#fff" stroke-width="4"/>
      </svg>
      <div class="pipe-art" role="img" aria-label="White bagpipe icon"></div>
    </div>
    <div class="icon-tile icon-repeat">
      <svg viewBox="0 0 236 236" aria-hidden="true">
        <rect x="3" y="3" width="230" height="230" rx="24" fill="#111" stroke="#fff" stroke-width="4"/>
        <g fill="none" stroke="#fff" stroke-width="20" stroke-linecap="butt">
          <path d="M62 112 A56 56 0 0 1 160 80"/>
          <path d="M174 124 A56 56 0 0 1 76 156"/>
        </g>
        <g fill="#fff">
          <path d="M140 62 L188 60 L176 108 Z"/>
          <path d="M96 174 L48 176 L60 128 Z"/>
        </g>
      </svg>
    </div>
  </aside>

  <div class="bagpipe-ghost" role="img" aria-label="Faint grey silhouette of a set of bagpipes"></div>

  <div class="author-tab">DARA COLBY</div>

  <h1 class="title">
    <span class="title-word word-1">WAKE</span>
    <span class="title-word word-2">STROLL</span>
    <span class="title-word word-3">HUM</span>
    <span class="title-word word-4">AGAIN</span>
  </h1>

  <footer class="subtitle-bar">MUSIC FOR THE BAGPIPES</footer>
</main>
</body>
</html>
```